Letterhead

I would like a standard letter head document that is innovative and not 'typically' corporate.
I would like a BLACK panel of some sort so that the logo can be best showcased within that (as the logo has a black background).
I would like the three words 'dream', 'believe', 'achieve'
inscribed at the side (as per the example I uploaded). Its should be more like a watermark so only just visible.
I would like the K symbol as a water mark on the page (similar to the lion on the example I uploaded).
I would like the following details also included.
Lydia Thornbury
Personal Training/Nutrition/Life Coaching
www.strongandsteady.com.au
0417 256 094

```html
<!DOCTYPE html>
<html lang="en">
<head>
<meta charset="utf-8">
<title>Strong and Steady Stationery</title>
<link rel="stylesheet" href="https://fonts.googleapis.com/css2?family=Open+Sans:wght@400;700&display=swap">
<style>
  :root {
    --ink: #111111;
    --teal: #17a3a5;
    --paper: #ffffff;
    --backdrop: #d6d6d6;
    --edge: #c4c4c4;
    --mark: #ececec;
    --white: #ffffff;
  }
  * { margin: 0; padding: 0; box-sizing: border-box; }
  html, body { width: 1200px; height: 849px; overflow: hidden; }
  body {
    background: var(--backdrop);
    font-family: "Open Sans", Arial, sans-serif;
    position: relative;
  }
  .sheet, .envelope {
    position: absolute;
    background: var(--paper);
    overflow: hidden;
  }
  .sheet { left: 132px; top: 51px; width: 468px; height: 660px; }
  .envelope {
    left: 537px; top: 260px; width: 510px; height: 244px;
    outline: 1px solid var(--edge);
  }
  .shapes { position: absolute; inset: 0; width: 100%; height: 100%; }
  .shape-ink { fill: var(--ink); }
  .shape-teal { fill: var(--teal); }

  .brand-name {
    position: absolute;
    color: var(--teal);
    font-weight: 700;
    white-space: nowrap;
    display: flex;
    align-items: center;
    gap: 8px;
  }
  .brand-dot {
    width: 10px; height: 10px; border-radius: 50%;
    background: var(--teal);
  }
  .sheet .brand-name { left: 24px; top: 38px; font-size: 25px; }
  .envelope .brand-name { left: 26px; top: 20px; font-size: 22px; }

  .contact { position: absolute; color: var(--ink); line-height: 1.25; }
  .contact .person { font-weight: 700; font-size: 10px; }
  .contact .line { font-size: 6.5px; }
  .sheet .contact { left: 334px; top: 24px; }

  .envelope .contact {
    left: 33px; width: 246px; top: 212px;
    text-align: center; color: var(--white);
    line-height: 1.15;
  }
  .envelope .contact .person { font-size: 8.5px; }
  .envelope .contact .line { font-size: 5.5px; }

  .watermark {
    position: absolute;
    left: 108px; top: 115px; width: 220px; height: 492px;
    background: linear-gradient(180deg, var(--mark), #f6f6f6);
    border-radius: 110px 110px 40px 40px;
    opacity: 0.8;
  }
  .footer-web {
    position: absolute;
    left: 107px; width: 252px; bottom: 6px;
    text-align: center;
    color: var(--white);
    font-size: 6.5px; font-weight: 700;
  }
</style>
</head>
<body>

<section class="sheet" aria-label="Letterhead">
  <svg class="shapes" viewBox="0 0 468 660" preserveAspectRatio="none" aria-hidden="true">
    <polygon class="shape-ink" points="0,0 468,0 468,80 0,128"/>
    <polygon class="shape-teal" points="331,0 468,0 468,80 310,96"/>
    <ellipse class="shape-ink" cx="233" cy="662" rx="126" ry="22"/>
  </svg>
  <div class="brand-name"><span class="brand-dot"></span>Strong and Steady</div>
  <div class="contact">
    <p class="person">Lydia Thornbury</p>
    <p class="line">Personal Training/Nutrition/Life Coaching</p>
    <p class="line">www.strongandsteady.com.au</p>
    <p class="line">0417 256 094</p>
  </div>
  <div class="watermark" role="img" aria-label="Faint brand symbol watermark"></div>
  <p class="footer-web">www.strongandsteady.com.au</p>
</section>

<section class="envelope" aria-label="Envelope">
  <svg class="shapes" viewBox="0 0 510 244" preserveAspectRatio="none" aria-hidden="true">
    <polygon class="shape-ink" points="0,0 510,0 510,15 0,94"/>
    <polygon class="shape-teal" points="341,0 510,0 510,15 333,42"/>
    <ellipse class="shape-ink" cx="156" cy="248" rx="124" ry="48"/>
  </svg>
  <div class="brand-name"><span class="brand-dot"></span>Strong and Steady</div>
  <div class="contact">
    <p class="person">Lydia Thornbury</p>
    <p class="line">Personal Training/Nutrition/Life Coaching</p>
    <p class="line">www.strongandsteady.com.au</p>
    <p class="line">0417 256 094</p>
  </div>
</section>

</body>
</html>
```